We are seeking two label designs for our premium pecan snack brand, MORVELO. MORVELO is known for its innovative pecan snacks, specifically a healthy and exotic blend of pecans, expertly salted, and infused with unique chili flavors. Our snacks are packaged in stand-up pouch bags, and we are looking for label designs product sizes - 5 oz. ( Size: 14 x 20 cm / 5.5 x 7.8 inches / Max Capacity: 16.2 oz)

Background Information:
MORVELO is a brand committed to offering a delightful snacking experience that combines the natural richness of pecans with the bold and exotic kick of carefully selected chilies. Our snacks cater to health-conscious consumers who appreciate the fusion of premium quality, unique flavors, and nutritional goodness.

Target Market(s)

Event Attendees (Entertainment Industry), Health-Conscious Consumers

Industry/Entity Type

Entertainment (sports events, arenas, stadiums, etc)

Font styles to use
Other font styles liked:
• Brother1816 Printed

Colors

Designer to choose colors to be used in the design.

Requirements
Must have
• Nutrition Fact (attached) , TRANSPARENT PART LIKE A WINDOW TO DISPLAY THE PRODUCT

```html
<!DOCTYPE html>
<html lang="en">
<head>
<meta charset="utf-8">
<title>MORVELO – Spicy Roasted Pecans Pouch Label</title>
<link rel="stylesheet" href="https://fonts.googleapis.com/css2?family=Montserrat:wght@400;500&family=Staatliches&display=swap">
<style>
  :root {
    --backdrop: #949494;
    --pouch-black: #141414;
    --ember-orange: #d4622f;
    --banner-orange: #d9693a;
    --cream: #f2ebe4;
    --white: #ffffff;
    --zip-line: #3a3a3a;
    --pecan-light: #c98d5c;
    --pecan-dark: #8a4f2a;
  }
  * { margin: 0; padding: 0; box-sizing: border-box; }
  html, body {
    width: 1200px;
    height: 800px;
    overflow: hidden;
    background: var(--backdrop);
  }
  .canvas {
    position: relative;
    width: 1200px;
    height: 800px;
    background: var(--backdrop);
  }
  .pouch {
    position: absolute;
    left: 391px;
    top: 82px;
    width: 410px;
    height: 648px;
    border-radius: 14px;
    overflow: hidden;
    background: var(--pouch-black);
  }
  .pouch-shapes {
    position: absolute;
    inset: 0;
    width: 410px;
    height: 648px;
  }
  .brand-name {
    position: absolute;
    top: 122px;
    left: 0;
    width: 410px;
    text-align: center;
    font-family: "Montserrat", sans-serif;
    font-weight: 500;
    font-size: 46px;
    letter-spacing: 2px;
    color: var(--white);
  }
  .brand-byline {
    position: absolute;
    top: 175px;
    right: 122px;
    font-family: "Montserrat", sans-serif;
    font-weight: 400;
    font-size: 9px;
    letter-spacing: 0.5px;
    color: var(--white);
  }
  .product-title {
    position: absolute;
    top: 228px;
    left: 63px;
    width: 281px;
    text-align: center;
    font-family: "Staatliches", sans-serif;
    font-size: 37px;
    line-height: 36px;
    color: var(--cream);
  }
  .net-weight {
    position: absolute;
    top: 583px;
    left: 0;
    width: 410px;
    text-align: center;
    font-family: "Montserrat", sans-serif;
    font-weight: 400;
    font-size: 10px;
    letter-spacing: 0.5px;
    color: var(--white);
  }
</style>
</head>
<body>
<main class="canvas">
  <section class="pouch">
    <svg class="pouch-shapes" viewBox="0 0 410 648" xmlns="http://www.w3.org/2000/svg">
      <defs>
        <radialGradient id="pecanFill" cx="50%" cy="45%" r="60%">
          <stop offset="0%" stop-color="var(--pecan-light)"/>
          <stop offset="100%" stop-color="var(--pecan-dark)"/>
        </radialGradient>
      </defs>
      <!-- zipper seal -->
      <line class="zip-line" x1="20" y1="82" x2="390" y2="82" stroke="var(--zip-line)" stroke-width="2"/>
      <line class="zip-line" x1="20" y1="94" x2="390" y2="94" stroke="var(--zip-line)" stroke-width="1.5"/>
      <!-- bottom sweep -->
      <path class="sweep-white" d="M0 428 Q205 575 410 436 L410 648 L0 648 Z" fill="var(--white)"/>
      <path class="sweep-orange" d="M0 462 Q205 610 410 454 L410 648 L0 648 Z" fill="var(--ember-orange)"/>
      <!-- product window -->
      <ellipse class="product-window" cx="203" cy="438" rx="133" ry="125" fill="url(#pecanFill)"
               role="img" aria-label="Window showing roasted pecan halves inside the pouch"/>
      <!-- title banner -->
      <path class="title-banner" d="M66 218 L346 214 L344 258 L345 306 Q205 300 63 314 L64 266 Z" fill="var(--banner-orange)"/>
      <line x1="72" y1="226" x2="340" y2="222" stroke="var(--cream)" stroke-width="1.5"/>
      <path d="M74 306 Q205 294 336 298" fill="none" stroke="var(--cream)" stroke-width="1.5"/>
    </svg>
    <h1 class="brand-name">MORVELO</h1>
    <p class="brand-byline">BY TALVERN</p>
    <h2 class="product-title">Spicy Roasted<br>Pecans</h2>
    <p class="net-weight">8 oz (227gr)</p>
  </section>
</main>
</body>
</html>
```